Marrowgate Auctions Business Cards Design Needed

I need a business card design that is modern looking - double sided (maybe just my logo on the back, but open to suggestions) - the overall design is up to you. I want it to be easy to read - not over the top flashy. I already have a company logo which I uploaded so that needs to be used. The colors of my logo are the colors I want on the card... so blue and gray (do need to match the logo colors).

Requirements
Must have
• Would like the card to be sleek, modern and easy to ready

```html
<!DOCTYPE html>
<html lang="en">
<head>
<meta charset="utf-8">
<title>Marrowgate Auctions – Business Cards</title>
<link rel="stylesheet" href="https://fonts.googleapis.com/css2?family=Roboto:wght@400;500;700&display=swap">
<style>
  :root {
    --stage: #2b2b2d;
    --card-gray: #5b5b5e;
    --brand-blue: #2a72b8;
    --brand-blue-light: #3d86cc;
    --brand-gray: #55565a;
    --white: #ffffff;
  }
  * { margin: 0; padding: 0; box-sizing: border-box; }
  html, body {
    width: 1200px; height: 768px; overflow: hidden;
    background: var(--stage);
    font-family: "Roboto", sans-serif;
  }
  .stage { position: relative; width: 1200px; height: 768px; }
  .card {
    position: absolute; top: 230px;
    width: 540px; height: 309px;
    overflow: hidden;
    box-shadow: 0 10px 30px rgba(0,0,0,.45);
  }
  /* Back side */
  .card-back { left: 40px; background: var(--card-gray); }
  .card-back .brand-name {
    position: absolute; left: 0; right: 0; top: 118px;
    text-align: center;
    color: var(--white);
    font-weight: 700; font-size: 30px; letter-spacing: 2px;
    text-transform: uppercase;
  }
  .card-back .tagline {
    position: absolute; left: 0; right: 0; bottom: 40px;
    text-align: center;
    color: var(--white); font-size: 12px; letter-spacing: 1px;
  }
  /* Front side */
  .card-front { left: 620px; background: var(--white); }
  .front-brand {
    position: absolute; left: 40px; top: 62px;
    display: flex; align-items: center; gap: 12px;
  }
  .front-brand .brand-mark {
    width: 34px; height: 34px; background: var(--brand-blue);
  }
  .front-brand .brand-name {
    color: var(--brand-gray);
    font-weight: 700; font-size: 26px; letter-spacing: 1px;
    text-transform: uppercase;
  }
  .card-wave { position: absolute; inset: 0; width: 540px; height: 309px; }
  .contact-block {
    position: absolute; right: 24px; top: 196px;
    text-align: right; color: var(--white);
  }
  .contact-block .person-name {
    font-weight: 700; font-size: 20px; letter-spacing: 1px;
    text-transform: uppercase; line-height: 1.1;
  }
  .contact-block .person-role {
    font-weight: 500; font-size: 11.5px; margin-bottom: 7px;
  }
  .contact-line {
    display: flex; justify-content: flex-end; align-items: center; gap: 7px;
    font-size: 12px; line-height: 17px;
  }
  .contact-line svg { width: 11px; height: 11px; fill: var(--white); }
</style>
</head>
<body>
<main class="stage">
  <section class="card card-back" aria-label="Card back">
    <div class="brand-name">Marrowgate</div>
    <div class="tagline">Improving Online Sales</div>
  </section>

  <section class="card card-front" aria-label="Card front">
    <div class="front-brand">
      <span class="brand-mark"></span>
      <span class="brand-name">Marrowgate Auctions</span>
    </div>

    <svg class="card-wave" viewBox="0 0 540 309" aria-hidden="true">
      <defs>
        <linearGradient id="waveFill" x1="0" y1="0" x2="1" y2="0">
          <stop offset="0" stop-color="#5b9bd6"/>
          <stop offset="0.35" stop-color="#2a72b8"/>
          <stop offset="1" stop-color="#2a72b8"/>
        </linearGradient>
      </defs>
      <path d="M135 309 C 240 215, 400 180, 540 190 L540 309 Z" fill="url(#waveFill)"/>
      <path d="M110 300 C 240 200, 420 160, 540 178 C 420 170, 250 205, 110 300 Z" fill="var(--brand-blue)"/>
    </svg>

    <div class="contact-block">
      <div class="person-name">Owen Hartley</div>
      <div class="person-role">Owner/President - Auctioneer</div>
      <div class="contact-line">702-555-0148
        <svg viewBox="0 0 24 24"><path d="M6.6 10.8a15.1 15.1 0 0 0 6.6 6.6l2.2-2.2a1 1 0 0 1 1-.25 11.4 11.4 0 0 0 3.6.57 1 1 0 0 1 1 1V20a1 1 0 0 1-1 1A17 17 0 0 1 3 4a1 1 0 0 1 1-1h3.5a1 1 0 0 1 1 1c0 1.25.2 2.45.57 3.6a1 1 0 0 1-.25 1z"/></svg>
      </div>
      <div class="contact-line">marrowgate@mail.com
        <svg viewBox="0 0 24 24"><path d="M2 5h20v14H2z M2 5l10 8 10-8" /></svg>
      </div>
      <div class="contact-line">www.gavelrelay.com
        <svg viewBox="0 0 24 24"><circle cx="12" cy="12" r="10"/></svg>
      </div>
    </div>
  </section>
</main>
</body>
</html>
```